Flyer Design for Business: "Velvet Glow"

My Business name is "VELVET GLOW"

Laser Hair Removal
Non invasive and pain free
Look amazing and feel confident with a Hair Free body
Now is the time to start don't delay
1 treatment a month will ensure you are bikini hot for the summer months
Take full advantage of our OPENING SPECIALS of 30%-40% savings
Part payments available

CELLULITE & FAT REDUCTION
Now you too can look amazing without invasive surgery, downtime or discomfort
Tara Wellbrook & Monica Farrowdale are avid recipients of this treatment.
Effective on all skin types and delivers fast measurable results for:
Helping mums regain their pre-baby figures
Losing the love handles (but keeping the love)
Stretch mark reduction
Skin tightening
Cellulite busting on Arms, tummy, thighs.
Man boob reduction.
Latest technology:
Bi Polar radio frequency (RF)
infrared light
negative pressure (Vacuum)
Tissue manipulation through roller mechanical massage.
50% saving Call now

PDT LED REJUVENATION LIGHT THERAPY
ORVA Researchers found:
Fibroblast and muscles grew 5 times faster, stimulates
reconstruction of collagenous fibres of the dermis
These findings and more assist with:
Remove freckles, sunburn pigmentation,
Cures acne and hair follicle inflammation
Anti aging skin tightening
Reduces pore size
Improve the skin texture
Improves circulation
Red light : reduces pore size, softens skin wrinkles,reduces acne
Blue light: Kills the acne bacillus to eliminate acne, inhibit inflammation
Yellow light: Skin tightening, whitening and softens skin wrinkles
Purple light: combination of red & blue lights treats acne scars
Orange light increases cell energy and accelerates metabolism
$55 Saving and relax under the lights.

Who can resist a soothing Hot stone massage therapy after:
A hard stressful day at work
Aches and muscular pain

Pick anything from this info with a couple of nice images.

Target Market(s)

Females & males Sports minded people cyclists

Industry/Entity Type

Beauty Salon

Colors
00a990
e34197

Requirements
Must have
• a couple of images and
Nice to have
• Pink and bluey green like my business card

```html
<!DOCTYPE html>
<html lang="en">
<head>
<meta charset="utf-8">
<title>Velvet Glow Beauty Salon Flyer</title>
<link rel="stylesheet" href="https://fonts.googleapis.com/css2?family=Open+Sans:wght@400;600;700;800&family=Teko:wght@400;500&display=swap">
<style>
  :root {
    --pink: #e34197;
    --pink-deep: #c92a80;
    --teal: #00a990;
    --teal-light: #5ec9b6;
    --white: #ffffff;
    --paper: #f3f3f4;
    --ink-teal: #14a48c;
  }
  html, body {
    margin: 0;
    padding: 0;
    overflow: hidden;
  }
  .flyer {
    position: relative;
    width: 900px;
    height: 1200px;
    overflow: hidden;
    background: linear-gradient(180deg, #fbfbfb 0%, var(--paper) 60%, #e9e9ea 100%);
    font-family: "Open Sans", Arial, sans-serif;
  }
  .backdrop {
    position: absolute;
    inset: 0;
  }
  .brand {
    position: absolute;
    left: 60px;
    top: 34px;
    width: 444px;
    height: 152px;
    border-radius: 0 0 14px 14px;
    background: linear-gradient(180deg, #ee6fb2 0%, var(--pink) 55%, var(--pink-deep) 100%);
    box-shadow: 0 6px 10px rgba(0,0,0,0.25);
    border: 3px solid var(--white);
    border-top: none;
    color: var(--white);
    text-align: center;
  }
  .brand-name {
    margin: 22px 0 0;
    font-size: 58px;
    font-weight: 800;
    letter-spacing: 0.5px;
    line-height: 1;
  }
  .brand-tag {
    margin: 8px 0 0;
    font-size: 38px;
    font-weight: 400;
    line-height: 1;
  }
  .offer {
    position: absolute;
    left: 309px;
    top: 336px;
    width: 260px;
    text-align: center;
    color: var(--white);
    white-space: nowrap;
  }
  .offer-lead {
    font-family: "Teko", "Arial Narrow", sans-serif;
    font-size: 32px;
    line-height: 1;
    font-weight: 500;
  }
  .offer-lead small {
    font-family: "Open Sans", Arial, sans-serif;
    font-size: 18px;
    font-weight: 400;
  }
  .offer-amount {
    font-size: 36px;
    font-weight: 800;
    color: var(--pink);
    line-height: 1.1;
  }
  .offer-word {
    font-size: 32px;
    font-weight: 400;
    line-height: 1;
  }
  .heading {
    font-family: "Teko", "Arial Narrow", sans-serif;
    font-weight: 500;
    text-transform: uppercase;
    line-height: 1;
    margin: 0;
    white-space: nowrap;
  }
  .cellulite {
    position: absolute;
    left: 74px;
    top: 604px;
    width: 356px;
  }
  .cellulite .heading {
    color: var(--pink);
    font-size: 36px;
    text-shadow: 1px 1px 0 #8f1c58;
  }
  .cellulite p {
    margin: 12px 0 0;
    color: var(--ink-teal);
    font-size: 15.5px;
    line-height: 1.4;
    text-align: justify;
  }
  .cellulite .benefits {
    margin-top: 2px;
    font-size: 14.5px;
    font-weight: 700;
    line-height: 1.45;
    text-align: left;
  }
  .therapy {
    position: absolute;
    left: 452px;
    top: 580px;
    width: 420px;
    color: var(--white);
  }
  .therapy .heading {
    color: var(--teal);
    font-size: 35px;
    text-shadow: 1px 1px 0 #006b5b;
  }
  .therapy p {
    margin: 16px 0 0;
    font-size: 15px;
    line-height: 1.3;
    text-align: justify;
  }
  .lights {
    list-style: none;
    margin: 8px 0 0;
    padding: 0;
    font-size: 16.5px;
    line-height: 1.3;
  }
  .lights li {
    position: relative;
    padding-left: 22px;
    margin-bottom: 4px;
  }
  .lights li::before {
    content: "";
    position: absolute;
    left: 2px;
    top: 8px;
    width: 7px;
    height: 7px;
    border-radius: 50%;
    background: var(--teal);
  }
  .lights b { font-weight: 700; }
  .laser {
    position: absolute;
    left: 74px;
    top: 990px;
    color: var(--white);
    font-size: 22px;
    line-height: 1.22;
    margin: 0;
  }
  .call-out {
    position: absolute;
    left: 60px;
    top: 1116px;
    width: 820px;
  }
  .call-out .heading {
    color: var(--pink);
    font-size: 30px;
    text-shadow: 1px 1px 0 #7e1650;
  }
</style>
</head>
<body>
<main class="flyer">
  <svg class="backdrop" width="900" height="1200" viewBox="0 0 900 1200">
    <defs>
      <linearGradient id="hairPhoto" x1="0" y1="0" x2="1" y2="1">
        <stop offset="0" stop-color="#f4e6df"/>
        <stop offset="0.35" stop-color="#d9643a"/>
        <stop offset="0.7" stop-color="#b1431f"/>
        <stop offset="1" stop-color="#f6eae6"/>
      </linearGradient>
      <linearGradient id="portraitDark" x1="0" y1="0" x2="1" y2="1">
        <stop offset="0" stop-color="#3b2a26"/>
        <stop offset="0.5" stop-color="#c9a196"/>
        <stop offset="1" stop-color="#4a332c"/>
      </linearGradient>
      <linearGradient id="portraitBlonde" x1="0" y1="0" x2="1" y2="1">
        <stop offset="0" stop-color="#efe0c4"/>
        <stop offset="0.55" stop-color="#cdb48a"/>
        <stop offset="1" stop-color="#1e1a1a"/>
      </linearGradient>
      <linearGradient id="tealBand" x1="0" y1="0" x2="1" y2="0">
        <stop offset="0" stop-color="#2fb9a2"/>
        <stop offset="1" stop-color="#8ad8ca"/>
      </linearGradient>
      <linearGradient id="pinkPanel" x1="0" y1="0" x2="1" y2="1">
        <stop offset="0" stop-color="#e24c9c"/>
        <stop offset="1" stop-color="#f08fc2"/>
      </linearGradient>
      <radialGradient id="offerDisc" cx="0.5" cy="0.4" r="0.6">
        <stop offset="0" stop-color="#35c0a9"/>
        <stop offset="1" stop-color="#079c85"/>
      </radialGradient>
      <linearGradient id="eyeSoft" x1="0" y1="0" x2="1" y2="0">
        <stop offset="0" stop-color="#f6f6f6" stop-opacity="0"/>
        <stop offset="0.5" stop-color="#e4e4e6"/>
        <stop offset="1" stop-color="#f6f6f6" stop-opacity="0"/>
      </linearGradient>
      <clipPath id="clipLeft"><circle cx="203" cy="392" r="160"/></clipPath>
      <clipPath id="clipBlonde"><circle cx="704" cy="1002" r="116"/></clipPath>
    </defs>

    <rect class="photo-eye" x="300" y="120" width="380" height="460" fill="url(#eyeSoft)" role="img" aria-label="Faint close-up of an eye with long lashes"/>

    <rect class="photo-hair" x="520" y="0" width="380" height="510" fill="url(#hairPhoto)" role="img" aria-label="Woman with sleek copper red hair, looking down"/>

    <path class="wave-top-teal" d="M330 520 C 520 440, 700 470, 900 520 L900 560 C 700 500, 520 480, 330 560 Z" fill="var(--teal)"/>
    <path class="wave-top-pink" d="M330 540 C 520 480, 700 500, 900 540" fill="none" stroke="var(--pink)" stroke-width="4"/>

    <path class="panel-pink" d="M418 560 C 560 520, 740 520, 900 560 L900 910 Q900 934 876 934 L442 934 Q418 934 418 910 Z" fill="url(#pinkPanel)"/>

    <path class="wave-left" d="M0 540 C 120 620, 260 600, 420 560" fill="none" stroke="var(--teal)" stroke-width="10"/>
    <path class="wave-left-pink" d="M0 552 C 120 632, 260 612, 420 572" fill="none" stroke="var(--pink)" stroke-width="3"/>

    <circle cx="203" cy="392" r="168" fill="var(--pink)"/>
    <circle cx="203" cy="392" r="163" fill="var(--white)"/>
    <rect x="30" y="220" width="350" height="350" fill="url(#portraitDark)" clip-path="url(#clipLeft)" role="img" aria-label="Portrait of a woman with long dark curls and red lipstick"/>

    <circle cx="439" cy="395" r="132" fill="var(--pink)"/>
    <circle cx="439" cy="395" r="126" fill="var(--white)"/>
    <circle cx="439" cy="395" r="118" fill="url(#offerDisc)"/>

    <path class="band-bottom-pink" d="M0 936 C 220 886, 420 946, 620 1010 L900 1000" fill="none" stroke="var(--pink)" stroke-width="6"/>
    <path class="band-bottom" d="M0 952 C 220 902, 420 962, 620 1026 L900 1016 L900 1200 L0 1200 Z" fill="url(#tealBand)"/>

    <circle cx="704" cy="1002" r="126" fill="var(--pink)"/>
    <circle cx="704" cy="1002" r="120" fill="var(--white)"/>
    <rect x="580" y="880" width="250" height="250" fill="url(#portraitBlonde)" clip-path="url(#clipBlonde)" role="img" aria-label="Portrait of a woman with voluminous blonde curls"/>
  </svg>

  <header class="brand">
    <h1 class="brand-name">VELVET GLOW</h1>
    <p class="brand-tag">Beauty Salon</p>
  </header>

  <div class="offer">
    <div class="offer-lead">OPENING SPECIALS <small>of</small></div>
    <div class="offer-amount">30%-40%</div>
    <div class="offer-word">savings</div>
  </div>

  <section class="cellulite">
    <h2 class="heading">Cellulite &amp; Fat Reduction</h2>
    <p>Now you too can look amazing without invasive surgery, downtime or discomfort Tara Wellbrook &amp; Monica Farrowdale are avid recipients of this treatment. Effective on all skin types and delivers fast measurable results for: Helping mums regain their pre-baby figures Losing the love handles (but keeping the love)</p>
    <p class="benefits">Stretch mark reduction, Skin tightening<br>Cellulite busting on Arms, tummy, thighs.</p>
  </section>

  <section class="therapy">
    <h2 class="heading">PDT LED Rejuvenation Light Therapy</h2>
    <p>ORVA Researchers found:<br>Fibroblast and muscles grew 5 times faster, stimulates reconstruction of collagenous fibres of the dermis. These findings and more assist with:<br>Remove freckles, sunburn pigmentation,<br>Cures acne and hair follicle inflammation</p>
    <ul class="lights">
      <li><b>Red light :</b> reduces pore size, softens skin wrinkles,reduces acne</li>
      <li><b>Blue light:</b> Kills the acne bacillus to eliminate acne, inhibit inflammation</li>
      <li><b>Yellow light:</b> Skin tightening, whitening and softens skin wrinkles</li>
    </ul>
  </section>

  <p class="laser">Laser Hair Removal<br>Non invasive and pain free<br>Look amazing and feel<br>confident with a Hair Free body</p>

  <div class="call-out">
    <p class="heading">Now is the time to start don't delay</p>
    <p class="heading">1 treatment a month will ensure you are bikini hot for the summer months</p>
  </div>
</main>
</body>
</html>
```